Harrowell Partners need a double sided one page flyer/document designed

We need a double sided one page flyer/document design for Harrowell Partners Insurance Brokers Ltd designed to leave with potential prospects and Introducers. We are based in Birmingham City centre and offer commercial insurance and corporate protection for businesses. We would like to see the design colours the same as our website http://harrowellpartners-example.co.uk/ (Sky Blue) and should focus on our service, our constructive tailor made advice and our focus on Risk Management.

Reason: My Director is currently off until the 8th May and he gets the final sign off!

Target Market(s)

Larger Commercial Businesses mainly owner managed.

Industry/Entity Type

Insurance Broker

Colors
ffffff
85cae6
1b1b1b

Requirements
Must have
• 1) Our 2 tag lines are "Cover That Works...Not Worries" and "Our Craft....Is to grasp your Craft"
• 2) It must focus on our 4 key services which are "Corporate Protection / Risk Management / Claim & Risk Control and Health and Safety" and it must state that these are tailored to individual client needs. We would like a brief description about each of our key services (As per our website)
• 3) It must also have our 4 core values which are "Service / Partnership / Responsibility / Probity" We would like a brief description about each of our core values (As per our website)
• 4) It must explain a little about who we are and why we differ from the competition ie "due to our attention to detail, constructive advice, backed by robust risk management and comprehensive insurance protection"
• 5) Obviously our contact details. Harrowell Partners Insurance Brokers Ltd, 4th Floor, Calder Vale House, 42 Penmore Street, Birmingham B7 9QX 0121 478 2096
• 6) Our flyer content should read:
• Tag Line "Cover That Works....... Not Worries."
• Our 4 key services should read:
• "Corporate Protection : We take time to understand you and your business, evaluate your exposures and design a comprehensive protection programme to provide you with piece of mind and confidence.
• "Risk Management: We work with insurers to structure a Risk Management programme which can be self funding with potential future cost savings as a result of reduced exposures"
• "Claim & Risk Control; We have a team to provide support & technical advice aswell as access to experts where needed for any complex or specialist claims to help mitigate any loss"
• "Health & Safety: We have access to specialist services & will work in conjunction with consultants to ensure the most effective programme is implemented"
• Who we are: Harrowell Partners are recognised as a leading local insurance broker providing risk management and insurance solutions across the corporate and commercial sector. We adopt an entrepreneurial approach to the challenges that face our clients and are committed to the delivery of practical solutions.
• 2nd Tag line "Our Craft is to grasp your craft"
• Our 4 core values should read:
• "Service: We aim to deliver high levels of personal service which are designed to provide our clients with confidence that they will be looked after at all times. This is at the heart of everything we do"
• "Partnership: We view the relationship with our clients as a partnership, working together as a team in conjunction with insurers and Risk Managers"
• "Responsibility: We recognise that we have a responsibility and an obligation for all the services that we provide on our clients behalf"
• "Probity: We will endeavour to act with integrity and probity at all times"
Nice to have
• 1) A list of products we insure/cover.... Commercial Combined insurance / Directors & Offices insurance / Professional Indemnity Insurance / Employers and Public Liability / Products Liability / Motor Fleet insurance / Marine insurance / Cyber insurance / Engineering / Employment Protection / Personal Accident / Warranty & Indemnity cover.
• 2) A testimonial from our website on the Flyer
Should not have
• We do not insure personal lines insurance i.e. personal single vehicle insurance or small personal household insurance so no reference to any of these.

```html
<!DOCTYPE html>
<html lang="en">
<head>
<meta charset="utf-8">
<title>Harrowell Partners – Flyer</title>
<link rel="stylesheet" href="https://fonts.googleapis.com/css2?family=Arimo:ital,wght@0,400;0,700;1,400&family=Tinos:ital,wght@0,700;1,400&display=swap">
<style>
:root{
  --backdrop:#e8e9eb;
  --paper:#ffffff;
  --brand:#7a9fad;
  --ink:#1b1b1b;
  --text:#222222;
  --photo-warm-a:#6d5846;
  --photo-warm-b:#c49a74;
  --photo-cool-a:#e5e5e3;
  --photo-cool-b:#7c7f86;
}
*{box-sizing:border-box;margin:0;padding:0}
html,body{width:1200px;height:831px;overflow:hidden}
body{background:var(--backdrop);font-family:"Arimo",Arial,sans-serif;color:var(--text);position:relative}
.page{position:absolute;top:28px;width:550px;height:775px;background:var(--paper);box-shadow:0 1px 4px rgba(0,0,0,.25);overflow:hidden}
.page--front{left:32px}
.page--back{left:620px}
.abs{position:absolute}

/* Front header */
.brand{left:39px;top:30px;display:flex;align-items:center;gap:10px}
.brand__dot{width:46px;height:46px;border-radius:50%;background:var(--brand)}
.brand__name{font-size:24px;font-weight:400;color:var(--brand);line-height:1}
.contact{right:40px;top:40px;text-align:right;font-size:10.5px;line-height:15px;color:var(--ink)}
.contact__row{display:flex;justify-content:flex-end;align-items:center;gap:4px}
.contact__row svg{width:10px;height:10px}
.contact__phone{font-size:12px;font-weight:700}
.contact__role{font-size:7px;margin-top:2px}
.header-rule{left:0;top:103px;width:100%;height:3px;background:var(--brand)}

/* Photos */
.photo{left:0;width:100%}
.photo--meeting{top:106px;height:148px;background:linear-gradient(100deg,var(--photo-cool-a) 0%,#c9c8c6 35%,var(--photo-cool-b) 60%,#bfc0c2 100%)}
.photo--blocks{top:13px;height:241px;background:linear-gradient(110deg,#2c2622 0%,var(--photo-warm-a) 30%,var(--photo-warm-b) 55%,#d7b89b 75%,#b7cdd5 100%)}
.back-topbar{left:0;top:0;width:100%;height:13px;background:var(--brand)}

.tag{height:25px;color:#fff;font-weight:700;font-size:14.5px;display:flex;align-items:center;padding-left:14px}
.tag--dark{background:rgba(27,27,27,.8)}
.tag--light{background:rgba(122,159,173,.88)}

/* Services */
.services-intro{left:39px;top:270px;width:471px;height:28px;background:var(--ink);color:#fff;font-size:10px;display:flex;align-items:center;justify-content:center}
.services-frame{left:39px;top:298px;width:471px;height:288px;border:1px solid #9aa6ab;border-top:none}
.service{width:224px;height:134px;background:var(--brand);color:#fff;font-size:9.6px;line-height:12.6px}
.service__title{position:absolute;top:6px;height:17px;background:var(--ink);color:#fff;font-weight:700;font-size:9.6px;letter-spacing:.3px;display:flex;align-items:center}
.service--left .service__title{left:0;padding:0 26px 0 12px;clip-path:polygon(0 0,100% 0,calc(100% - 17px) 100%,0 100%)}
.service--right .service__title{right:0;padding:0 12px 0 26px;clip-path:polygon(0 0,100% 0,100% 100%,17px 100%)}
.service__body{position:absolute;top:40px}
.service--left .service__body{left:26px;width:170px}
.service--right .service__body{left:26px;width:176px;text-align:center}
.svc-a{left:45px;top:305px}
.svc-b{left:279px;top:305px}
.svc-c{left:45px;top:447px}
.svc-d{left:279px;top:447px}
.svc-c .service__body,.svc-d .service__body{top:38px}
.svc-d .service__body{text-align:left}
.hub{left:224px;top:394px;width:102px;height:102px;border-radius:50%;background:#fff;display:flex;align-items:center;justify-content:center}
.hub__mark{width:46px;height:46px;border-radius:50%;background:var(--brand)}

/* Who we are */
.section-title{font-weight:700;font-size:11px;letter-spacing:.4px;color:var(--ink)}
.who{left:39px;top:604px;width:302px}
.who p{font-size:9.8px;line-height:13.2px;margin-top:8px;color:var(--ink)}
.testimonial{left:354px;top:606px;width:156px;height:144px;background:#e4e6e7}
.testimonial__quote{padding:10px 10px 0 12px;font-family:"Tinos","Times New Roman",serif;font-style:italic;font-size:8.2px;line-height:11px;color:#333;height:106px}
.testimonial__by{position:absolute;left:0;bottom:0;width:100%;height:34px;background:var(--brand);padding:7px 8px 0 10px;font-family:"Tinos","Times New Roman",serif;font-size:8px;line-height:10.5px;color:var(--ink);white-space:nowrap}
.testimonial__by strong{font-weight:700}
.testimonial__by::before{content:"";position:absolute;right:14px;top:-8px;border-left:8px solid transparent;border-right:8px solid transparent;border-bottom:8px solid var(--brand)}

/* Back: philosophy */
.philosophy{left:40px;top:276px;width:475px}
.philosophy p{font-size:9.8px;line-height:13.4px;margin-top:8px;color:var(--ink)}
.value{width:231px;height:133px;border:2px solid var(--ink);background:#fff}
.value__head{position:absolute;top:9px;left:-2px;right:-2px;display:flex;align-items:center;gap:5px;font-weight:700;font-size:10.4px;color:var(--ink)}
.value__head::before{content:"";height:2px;background:var(--ink);width:14px}
.value__head::after{content:"";height:2px;background:var(--ink);flex:1}
.value--right .value__head::after{flex:0 0 14px}
.value--right .value__head::before{flex:1}
.value--right .value__head{justify-content:flex-end}
.value__head svg{width:13px;height:13px}
.value__body{position:absolute;top:36px;font-size:9.6px;line-height:12.6px;color:var(--ink)}
.value--left .value__body{left:26px;width:150px}
.value--right .value__body{left:26px;width:180px}
.val-a{left:40px;top:369px}
.val-b{left:280px;top:369px}
.val-c{left:40px;top:512px}
.val-d{left:280px;top:512px}
.val-c .value__head,.val-d .value__head{top:22px}
.val-c .value__body,.val-d .value__body{top:49px}
.core{left:219px;top:450px;width:112px;height:112px}
.core__label{position:absolute;left:24px;top:24px;width:64px;height:64px;border-radius:50%;background:var(--ink);color:#fff;font-weight:700;font-size:10.4px;line-height:11px;text-align:center;display:flex;align-items:center;justify-content:center}

/* Back footer */
.footer{left:40px;top:663px;width:471px;height:81px;background:var(--brand);color:#fff}
.footer__inner{position:absolute;left:12px;top:10px;width:378px;font-size:9px;line-height:12.4px}
.footer__lead{padding-bottom:5px;border-bottom:1px solid rgba(255,255,255,.7);margin-bottom:6px}
.footer__line{white-space:nowrap}
.footer__line--links{font-size:8.5px;letter-spacing:-.05px}
.footer__inner strong{font-weight:700}
.footer__mark{position:absolute;right:0;top:0;width:79px;height:81px;background:#fff;border:1px solid var(--brand);display:flex;align-items:center;justify-content:center}
.footer__mark span{width:40px;height:40px;border-radius:50%;background:var(--brand)}
</style>
</head>
<body>

<section class="page page--front">
  <header>
    <div class="abs brand"><span class="brand__dot"></span><span class="brand__name">harrowell partners</span></div>
    <div class="abs contact">
      <div class="contact__row contact__phone"><svg viewBox="0 0 10 10"><circle cx="5" cy="5" r="5" fill="#7a9fad"/><path d="M3.2 2.6c.4-.3.7 0 .9.4l.2.5c.1.3-.2.5-.3.7.3.6.7 1 1.3 1.3.2-.1.4-.4.7-.3l.5.2c.4.2.7.5.4.9-.4.6-1.2.6-2 .1-.9-.6-1.6-1.3-2-2.2-.3-.7-.3-1.3.3-1.6z" fill="#fff"/></svg>0121 478 2096</div>
      <div class="contact__row"><svg viewBox="0 0 10 10"><circle cx="5" cy="5" r="5" fill="#7a9fad"/><rect x="2.5" y="3.2" width="5" height="3.6" fill="none" stroke="#fff" stroke-width=".8"/><path d="M2.5 3.4 5 5.3l2.5-1.9" fill="none" stroke="#fff" stroke-width=".8"/></svg>info@harrowellpartners-example.co.uk</div>
      <div class="contact__role">Insurance Brokers &amp; Risk Management Consultants</div>
    </div>
    <div class="abs header-rule"></div>
  </header>

  <div class="abs photo photo--meeting" role="img" aria-label="Photograph of business people shaking hands in a bright meeting room"></div>
  <div class="abs tag tag--dark" style="left:88px;top:169px;width:185px">Cover That Works...</div>
  <div class="abs tag tag--light" style="left:275px;top:169px;width:187px">Not Worries...</div>

  <div class="abs services-intro">A brief Outline of our key services are summarised below which we tailor to your individual needs:</div>
  <div class="abs services-frame"></div>

  <article class="abs service service--left svc-a">
    <h3 class="service__title">CORPORATE PROTECTION</h3>
    <p class="service__body">We take time to understand you is your business, evaluate your exposure and design a programme of comprehensive protection designed to provide you with piece of mind and confidence</p>
  </article>
  <article class="abs service service--right svc-b">
    <h3 class="service__title">RISK MANAGEMENT</h3>
    <p class="service__body">We work with insurers to structure a risk management programme which can be self funding with future cost savings as a result of reduced exposures</p>
  </article>
  <article class="abs service service--left svc-c">
    <h3 class="service__title">CLAIM &amp; RISK CONTROL</h3>
    <p class="service__body">We have a local claims team to provide support &amp; technical advice, aswell as access to experts where needed for any complex or specialist claims. They will help you to mitigate your loss</p>
  </article>
  <article class="abs service service--right svc-d">
    <h3 class="service__title">HEALTH AND SAFETY</h3>
    <p class="service__body">We have access to specialist services &amp; will work in conjuction with consultants to ensure the most effective programme is implemented</p>
  </article>
  <div class="abs hub"><span class="hub__mark"></span></div>

  <section class="abs who">
    <h2 class="section-title">WHO WE ARE</h2>
    <p>Harrowell Partners are recognized as a leading local insurance broker providing risk management and insurance solutions across the corporate and commercial sector.</p>
    <p>Adopting an entrepreneurial approach to the challenges that face our clients and are commited to the delivery of practical solutions. We differ from competition with our attention to detail, constructive advice, backed by robust risk management and comprehensive insurance protection. We never compromise on the need to be competitive on price.</p>
  </section>

  <aside class="abs testimonial">
    <p class="testimonial__quote">We have dealt with the team at Harrowell's for in excess of 10 years, they have delivered on costs consistently and have always been available for advice and support when needed. The are a trusted supplier to our business, I know we are in safe hand with them</p>
    <p class="testimonial__by"><strong>Rhys Calloway - Managing Director</strong><br>Brindlecast Tools Limited</p>
  </aside>
</section>

<section class="page page--back">
  <div class="abs back-topbar"></div>
  <div class="abs photo photo--blocks" role="img" aria-label="Photograph of a hand pulling a wooden block from a stacked block tower"></div>
  <div class="abs tag tag--dark" style="left:66px;top:109px;width:187px;height:22px;font-size:14px">Our Craft...</div>
  <div class="abs tag tag--light" style="left:66px;top:134px;width:254px;height:22px;font-size:14px">... is to grasp Your Craft</div>

  <section class="abs philosophy">
    <h2 class="section-title">OUR PHILOSOPHY</h2>
    <p>We see our relationship as a three way partnership between us, our clients and the insurers.<br>This enables us to deliver prompt and efficient service.</p>
    <p>We differ from the competition as we offer constructive advice, allied to a robust risk management strategy, offering comprehensive and competitive protection, backed up by a personal profesional service.</p>
  </section>

  <article class="abs value value--left val-a">
    <h3 class="value__head"><svg viewBox="0 0 14 14"><circle cx="7" cy="7" r="6.5" fill="#1b1b1b"/><path d="M7 2.6l1.2 2.8 3 .2-2.3 2 .7 3L7 9 4.4 10.6l.7-3-2.3-2 3-.2z" fill="#fff"/></svg>Service</h3>
    <p class="value__body">We aim to deliver high levels of personal service which are designed to provide our clients with confidence that they will be looked after at all times. This is at the heart of everything we do.</p>
  </article>
  <article class="abs value value--right val-b">
    <h3 class="value__head"><svg viewBox="0 0 14 14"><circle cx="7" cy="7" r="6.5" fill="#1b1b1b"/><circle cx="5" cy="6" r="1.6" fill="#fff"/><circle cx="9" cy="6" r="1.6" fill="#fff"/><path d="M2.6 10.5c.5-1.4 1.3-2 2.4-2s1.9.6 2 2zm4.4 0c.1-1.4.9-2 2-2s1.9.6 2.4 2z" fill="#fff"/></svg>Partnership</h3>
    <p class="value__body">We view the relationship with our clients as a partnership, working together as a team in conjunction with Insurers and Risk Managers.</p>
  </article>
  <article class="abs value value--left val-c">
    <h3 class="value__head"><svg viewBox="0 0 14 14"><circle cx="7" cy="7" r="6.5" fill="#1b1b1b"/><path d="M4.5 3.5h5v4.2c0 1.6-1.2 2.6-2.5 3-1.3-.4-2.5-1.4-2.5-3z" fill="#fff"/></svg>Responsibility</h3>
    <p class="value__body">We recognise that we have a responsibility and an obligation for all the services that we provide on our clients' behalf.</p>
  </article>
  <article class="abs value value--right val-d">
    <h3 class="value__head"><svg viewBox="0 0 14 14"><circle cx="7" cy="7" r="6.5" fill="#1b1b1b"/><path d="M3.5 6.5h1.6v4H3.5zm2.2 0 1.6-3c.7 0 1 .5.8 1.3l-.3 1.2h2.3c.6 0 .9.5.7 1l-1 2.6c-.2.5-.5.9-1 .9H5.7z" fill="#fff"/></svg>Probity</h3>
    <p class="value__body">We will endeavor to act with integrity and probity at all times.</p>
  </article>

  <div class="abs core">
    <svg viewBox="0 0 112 112" width="112" height="112" aria-hidden="true">
      <circle cx="56" cy="56" r="50" fill="#fff"/>
      <g fill="none" stroke="#1b1b1b" stroke-width="2.2">
        <path d="M60 10a46 46 0 0 1 42 42"/>
        <path d="M102 60a46 46 0 0 1-42 42"/>
        <path d="M52 102a46 46 0 0 1-42-42"/>
        <path d="M10 52a46 46 0 0 1 42-42"/>
      </g>
      <g fill="#1b1b1b">
        <path d="M102 52l-4-6h8z"/>
        <path d="M60 102l6-4v8z"/>
        <path d="M10 60l4 6H6z"/>
        <path d="M52 10l-6 4V6z"/>
      </g>
    </svg>
    <div class="core__label">OUR CORE<br>VALUES</div>
  </div>

  <footer class="abs footer">
    <div class="footer__inner">
      <p class="footer__lead">Please contact us to discuss your individual requirements:</p>
      <p class="footer__line"><strong>Harrowell</strong> Partners Insurance Brokers Limited</p>
      <p class="footer__line">Calder Vale House, 42 Penmore Street, Birmingham, B7 9QX</p>
      <p class="footer__line footer__line--links">0121 478 2096 | info@harrowellpartners-example.co.uk | www.harrowellpartners-example.co.uk</p>
    </div>
    <div class="footer__mark"><span></span></div>
  </footer>
</section>

</body>
</html>
```